business card for a massage therapy practice named 'Meadow and Willow Massage Studio'

I really need a trendy, yet easy on the eyes business card to complement my logo. Ideally with some gold or rose gold foil work.

My uploaded file of the logo I have in horizontal but I have a vertical version as well. Another color that is used in the website is a blush pink here and there. I'd like to see some trendy tropical leaves in the design.

```html
<!DOCTYPE html>
<html lang="en">
<head>
<meta charset="utf-8">
<title>Meadow and Willow Massage Studio – Business Card</title>
<link rel="stylesheet" href="https://fonts.googleapis.com/css2?family=Montserrat:wght@400;500&display=swap">
<style>
  :root {
    --stage: #e6e9ee;
    --mint: #a3dccb;
    --mint-deep: #8fd0bd;
    --paper: #f7f8f8;
    --mist: #e3e6e7;
    --ink: #1f2a29;
    --gold-light: #d8ccae;
    --gold: #b9a97f;
    --white: #ffffff;
  }
  * { margin: 0; padding: 0; box-sizing: border-box; }
  html, body { width: 1200px; height: 675px; overflow: hidden; }
  body {
    background: var(--stage);
    font-family: "Montserrat", sans-serif;
    color: var(--ink);
  }
  .canvas {
    position: relative;
    width: 1200px;
    height: 675px;
    display: flex;
    align-items: center;
    justify-content: center;
    gap: 30px;
  }
  .card {
    position: relative;
    width: 525px;
    height: 300px;
    overflow: hidden;
    border-radius: 3px;
    box-shadow: 0 10px 28px rgba(40, 55, 70, 0.16);
  }
  .card--front { background: var(--mint); }
  .card--back { background: var(--paper); }

  .brand {
    position: absolute;
    display: flex;
    align-items: center;
    gap: 10px;
  }
  .brand__dot {
    width: 16px; height: 16px;
    border-radius: 50%;
    background: var(--gold);
    flex: none;
  }
  .brand__name {
    font-weight: 500;
    font-size: 19px;
    line-height: 1.2;
    color: var(--ink);
    max-width: 230px;
  }
  .card--front .brand { left: 48px; top: 112px; }
  .card--back .brand { left: 30px; top: 32px; }
  .card--back .brand__name { font-size: 16px; max-width: 200px; }

  .foil-art {
    position: absolute;
    border-radius: 46% 54% 50% 50% / 60% 60% 40% 40%;
    background: radial-gradient(ellipse at 40% 60%, var(--gold-light), rgba(216, 204, 174, 0.35) 70%, rgba(216, 204, 174, 0) 100%);
  }
  .card--front .foil-art { right: -10px; top: 18px; width: 210px; height: 150px; }
  .card--back .foil-art { right: -6px; top: 20px; width: 200px; height: 150px; }

  .wave { position: absolute; inset: 0; width: 100%; height: 100%; }

  .contact {
    position: absolute;
    left: 30px;
    top: 112px;
  }
  .contact__person {
    font-size: 15px;
    color: var(--mint-deep);
    margin-bottom: 4px;
  }
  .contact__list { list-style: none; }
  .contact__item {
    display: flex;
    align-items: center;
    gap: 12px;
    font-size: 14px;
    line-height: 25px;
  }
  .contact__icon {
    width: 16px; height: 16px;
    border-radius: 50%;
    background: var(--mint-deep);
    display: flex; align-items: center; justify-content: center;
    flex: none;
  }
  .contact__icon svg { width: 10px; height: 10px; }

  .web {
    position: absolute;
    right: 40px;
    bottom: 36px;
    font-size: 14px;
    color: var(--white);
    letter-spacing: 0.3px;
    transform: rotate(-9deg);
    transform-origin: right bottom;
  }
</style>
</head>
<body>
<main class="canvas">

  <section class="card card--front" aria-label="Card front">
    <div class="foil-art" role="img" aria-label="Gold foil pineapple illustration"></div>
    <div class="brand">
      <span class="brand__dot"></span>
      <span class="brand__name">Meadow and Willow Massage Studio</span>
    </div>
  </section>

  <section class="card card--back" aria-label="Card back">
    <svg class="wave" viewBox="0 0 525 300" preserveAspectRatio="none" aria-hidden="true">
      <path d="M0 300 L0 270 C 120 210 330 190 525 110 L525 300 Z" fill="var(--mist)"/>
      <path d="M0 300 L0 296 C 130 240 340 215 525 140 L525 300 Z" fill="var(--mint)"/>
    </svg>
    <div class="foil-art" role="img" aria-label="Gold foil pineapple illustration"></div>

    <div class="brand">
      <span class="brand__dot"></span>
      <span class="brand__name">Meadow and Willow Massage Studio</span>
    </div>

    <div class="contact">
      <p class="contact__person">Dana Whitfield LMT</p>
      <ul class="contact__list">
        <li class="contact__item">
          <span class="contact__icon">
            <svg viewBox="0 0 10 10"><path d="M2 1 L3.6 1 L4.2 3 L3.2 3.8 C3.7 5 4.9 6.3 6.2 6.8 L7 5.8 L9 6.4 L9 8 C9 8.6 8.5 9 8 9 C4.5 8.7 1.3 5.5 1 2 C1 1.5 1.4 1 2 1 Z" fill="#fff"/></svg>
          </span>
          555.014.2287
        </li>
        <li class="contact__item">
          <span class="contact__icon">
            <svg viewBox="0 0 10 10"><rect x="1" y="2.2" width="8" height="5.6" fill="none" stroke="#fff" stroke-width="1"/><path d="M1 2.4 L5 5.4 L9 2.4" fill="none" stroke="#fff" stroke-width="1"/></svg>
          </span>
          meadowandwillow@mail.com
        </li>
        <li class="contact__item">
          <span class="contact__icon"></span>
          @meadowandwillow
        </li>
        <li class="contact__item">
          <span class="contact__icon"></span>
          @meadowandwillow
        </li>
      </ul>
    </div>

    <p class="web">www.meadowandwillow.com</p>
  </section>

</main>
</body>
</html>
```